dealcraftmentor.com - Podcast Guest Marketing E-Flyer PDF

Dear Designers:I am in need of an attractive and attention-getting layout and design for a three-page marketing flyer (commonly known as a media one sheet) that will be sent via e-mail, as PDF file, to various Podcast hosts to market me as a guest on their podcasts. I want the design of the document to "mirror" the design and branding on my parent dealcraftmentor.com website. I am providing ALL the edited and proofread copy and content - the designer just needs to create the design for this marketing document. I want an active PDF document and icons should be used for WorkLoop, Phone, E-mail , and website- with hyperlinks that connect accordingly. I need a fast turnaround.
Updates

Dear Designers - instead of using the photo in the project file of me speaking to the audience for the banner image - I thought it would be a better idea to make this marketing piece specific to Podcast Hosts. Therefore, an image such as the one in the link below would be good to use for a banner image. https://www.pixelvarnow.com/find?q=podcast+studio+photos&mode=img&ref=univ&id=Qm7TzRk2LwPa9XcNvB4eHyU8sDjF1gA5oE3iKtZ6bW0nMh&w=1377&h=804#pic=vrolapemxq3BcT:

Target Market(s)

This PDF document will be sent to 650 Podcast hosts in North America via a broadcast e-mail.

Font styles to use
Sans Serif

Colors
ec1f27
ffffff
000000
333333
9d9d9d

Requirements
Must have
• A three-page layout that is easy to navigate in PDF form.
• Proper font styles and sizes for key emphasis areas on the document/
• Consistent branding to mirror my dealcraftmentor.com parent website
• Must be easy for people to read
• Attention-getting design elements and layout
• Professional and sophisticated design
• Icons for contact information
Should not have
• Should not be cluttered and junky-looking.
• Should not use small font sizes that makes it difficult to read.
• If Podcast hosts are interested in having me as a guest - they will read the content as required on three-pages

```html
<!DOCTYPE html>
<html lang="en">
<head>
<meta charset="utf-8">
<title>Dealcraft Mentor – Testimonials</title>
<link href="https://fonts.googleapis.com/css2?family=Lato:ital,wght@0,300;0,400;0,700;1,300&display=swap" rel="stylesheet">
<style>
  :root{
    --brand-red:#ec1f27;
    --white:#ffffff;
    --black:#000000;
    --charcoal:#333333;
    --grey:#9d9d9d;
    --panel:#e9eaec;
    --rule:#c8c8c8;
  }
  *{margin:0;padding:0;box-sizing:border-box}
  html,body{width:856px;height:1200px;overflow:hidden;background:var(--white)}
  body{font-family:'Lato',sans-serif;color:var(--black);position:relative}
  .page{position:relative;width:856px;height:1200px}
  .brand{position:absolute;left:32px;top:36px;display:flex;align-items:center;gap:8px}
  .brand-mark{width:22px;height:22px;background:var(--brand-red)}
  .brand-name{font-size:20px;font-weight:400;color:var(--charcoal);letter-spacing:-.2px}
  .header-rule{position:absolute;left:0;top:86px;width:856px;height:1px;background:var(--rule)}
  .section-tag{position:absolute;left:44px;top:101px;width:231px;height:59px;background:var(--brand-red);border-radius:3px;color:var(--white);font-size:24px;font-weight:700;display:flex;align-items:center;justify-content:center}
  .feature-quote{position:absolute;left:44px;top:176px;width:768px;height:244px;background:var(--panel);border-radius:3px;padding:11px 21px}
  .feature-quote h2{font-size:16px;font-weight:400;margin-bottom:9px}
  .feature-quote h2 sup{font-size:9px}
  .quote{font-size:15.4px;font-weight:300;font-style:italic;line-height:24px;color:var(--charcoal)}
  .attribution{margin-top:24px;font-size:15.4px;line-height:24px;color:var(--charcoal);font-weight:300}
  .attribution strong{font-weight:400;color:var(--black)}
  .intro{position:absolute;left:44px;top:436px;width:700px;font-size:16px;line-height:24px;font-weight:400}
  .quote-list{position:absolute;left:44px;top:496px;width:764px;list-style:none}
  .quote-list li{margin-bottom:24px}
  .signature{position:absolute;left:44px;top:786px;font-size:15.4px;line-height:24px}
  .more{position:absolute;left:44px;top:908px;font-size:19px;font-weight:700}
  .more a{color:var(--brand-red);text-decoration:none;font-weight:400}
  .footer-band{position:absolute;left:12px;top:988px;width:832px;height:170px;background:var(--panel)}
  .cta{position:absolute;left:52px;top:965px;width:752px;height:52px;background:var(--brand-red);border-radius:3px;color:var(--white);font-size:25px;font-weight:700;display:flex;align-items:center;justify-content:center}
  .cta sup{font-size:13px}
  .contact{position:absolute;left:0;top:1033px;width:856px;text-align:center;font-size:16px;font-weight:700;line-height:24px;color:var(--black)}
  .contact a{color:inherit;text-decoration:none}
  .social{position:absolute;left:0;top:1116px;width:856px;display:flex;justify-content:center;gap:22px}
  .social a{color:var(--grey);font-size:14px;font-weight:700;text-decoration:none}
  .site-bar{position:absolute;left:12px;top:1158px;width:832px;height:31px;background:var(--charcoal);color:#d6d6d6;font-size:11px;display:flex;align-items:center;justify-content:center}
</style>
</head>
<body>
<div class="page">
  <header>
    <div class="brand"><span class="brand-mark"></span><span class="brand-name">dealcraftmentor</span></div>
    <div class="header-rule"></div>
  </header>

  <div class="section-tag">Testimonials</div>

  <section class="feature-quote">
    <h2>What Some Clients Are Saying About the Dealcraft Mentor<sup>®</sup></h2>
    <p class="quote">“Daniel Ashvale did a terrific job on my podcast. His negotiating insights and tips were well received by my listeners, and he was an engaging, knowledgeable, and entertaining guest. Given my expertise in real estate, I thought I was a good negotiator – until Daniel taught me a few new strategies and tips during the podcast. I would recommend Daniel to any podcast host – he is a pro and his topics are relevant and can benefit everyone.”</p>
    <p class="attribution"><strong>Corwin Pellett</strong><br>Podcast Host<br>Property Builders Roundtable Podcast, San Antonio, Texas</p>
  </section>

  <p class="intro">Below is a partial listing of testimonials from attendees at a Founders’ Circle (FC) event provided by the RT Dunmore, Chapter Learning Chair:</p>

  <ul class="quote-list">
    <li class="quote">“A very engaging, entertaining, and inspirational speaker who provided very useful information, strategies, and tips to apply to all my future negotiations.”</li>
    <li class="quote">“Thank you to FC Western New York for booking this speaker! I learned some things that I can address immediately and a lot material that I need to practice. Great session!”</li>
    <li class="quote">“Daniel was an outstanding speaker on the topic of negotiating! He was one of my favorite speakers ever! Daniel was a real ‘teacher’ versus other typical speakers who spend two hours bragging or promoting their book.”</li>
    <li class="quote">“Daniel was a very knowledgeable and well-prepared speaker who provided helpful tips and scripts throughout the entire presentation! I would love to learn more from this speaker.”</li>
  </ul>

  <p class="signature">RT Dunmore, CEO and President<br>Northgate Records Services<br>Founders’ Circle (FC) Western New York<br>Learning Chair</p>

  <p class="more">Read More Testimonials - <a href="#">Click Here</a></p>

  <footer>
    <div class="footer-band"></div>
    <div class="cta">Book Dealcraft Mentor<sup>®</sup>&nbsp;Daniel R. Ashvale for Your Podcast</div>
    <div class="contact">
      <a href="mailto:daniel@ashvalementor.com">E-mail: daniel@ashvalementor.com</a><br>
      <a href="tel:5550142738">Phone: 555-014-2738</a><br>
      <a href="#">WorkLoop Profile: workloop.com/in/danielashvale</a>
    </div>
    <nav class="social"><a href="#">WorkLoop</a><a href="#">Chirper</a><a href="#">FriendWall</a></nav>
    <div class="site-bar">www.dealcraftmentor.com</div>
  </footer>
</div>
</body>
</html>
```